Financial Planning business needs a new Business Card design

We need a business card design for an Australian financial planning business. I am looking for a clean simple design

Target Market(s)

People aged 25-40

Industry/Entity Type

Financial Service

Contact Information for Business Card

On the front of the card we need the following information:
Name: Colin Merrow (First Name Green: #006838 and last name Grey: #414042)
Position: Financial Adviser
Qualifications: BEc(Hons), AdDipFS(FP), Dip FMBM, CFL®
Mobile: 0437 512 604
Email: colin@brightledgeplan.com.au

On the back of the card we need:
Postal address: PO BOX 5307, PERTH BC, WA 6849
Website: www.brightledgeplan.com.au
Text: AFS Licence No. 518760

The fields need to be able to be edited.

Font styles to use
Sans Serif

Requirements
Must have
• Information listed above

```html
<!DOCTYPE html>
<html lang="en">
<head>
<meta charset="utf-8">
<title>Brightledge business card</title>
<link href="https://fonts.googleapis.com/css2?family=Open+Sans:wght@400;600;700&display=swap" rel="stylesheet">
<style>
  :root {
    --green: #006838;
    --grey: #414042;
    --charcoal: #3a3a3c;
    --paper: #ffffff;
    --backdrop: #e8eaea;
    --text: #3b3b3d;
  }
  * { box-sizing: border-box; margin: 0; padding: 0; }
  html, body { width: 1200px; height: 900px; overflow: hidden; }
  body {
    background: var(--backdrop);
    font-family: "Open Sans", Arial, sans-serif;
    color: var(--text);
    display: flex;
    align-items: center;
    justify-content: center;
    gap: 60px;
  }
  .card {
    position: relative;
    width: 525px;
    height: 300px;
    background: var(--paper);
    box-shadow: 0 2px 3px rgba(0,0,0,.08), 0 10px 24px rgba(0,0,0,.08);
    overflow: hidden;
  }
  .brand {
    position: absolute;
    display: flex;
    align-items: center;
    gap: 8px;
    font-weight: 700;
    font-size: 34px;
    letter-spacing: 0.5px;
    color: var(--green);
  }
  .brand-mark {
    width: 14px;
    height: 14px;
    background: var(--green);
  }
  /* back */
  .card-back .brand { left: 36px; top: 112px; }
  .card-back .shapes { position: absolute; inset: 0; }
  .company-details {
    position: absolute;
    left: 38px;
    top: 186px;
    font-size: 14.5px;
    line-height: 1.45;
    letter-spacing: 0.4px;
  }
  /* front */
  .card-front .brand { left: 40px; top: 208px; }
  .person {
    position: absolute;
    left: 290px;
    top: 40px;
  }
  .person-name {
    font-size: 27px;
    font-weight: 700;
    line-height: 1.05;
    color: var(--grey);
  }
  .person-name .first { color: var(--green); }
  .person-role {
    font-size: 14.5px;
    font-weight: 600;
    color: var(--grey);
    margin-bottom: 14px;
  }
  .person-quals, .person-contact {
    font-size: 13.5px;
    line-height: 1.4;
  }
  .person-quals { margin-bottom: 14px; }
  sup { font-size: 0.6em; }
</style>
</head>
<body>

  <section class="card card-back" aria-label="Card back">
    <svg class="shapes" width="525" height="300" viewBox="0 0 525 300" aria-hidden="true">
      <polygon points="300,0 525,0 525,175 375,98" fill="var(--charcoal)"/>
      <polygon points="375,98 525,175 525,300 445,300" fill="var(--green)"/>
    </svg>
    <div class="brand"><span class="brand-mark"></span>BRIGHTLEDGE</div>
    <address class="company-details" style="font-style: normal;">
      <div class="website">www.brightledgeplan.com.au</div>
      <div class="licence">AFS Licence No. 518760</div>
      <div class="postal">PO BOX 5307, PERTH BC, WA 6849</div>
    </address>
  </section>

  <section class="card card-front" aria-label="Card front">
    <div class="person">
      <div class="person-name"><span class="first">Colin</span> Merrow</div>
      <div class="person-role">Financial Adviser</div>
      <div class="person-quals">BEc(Hons), AdDipFS(FP)<br>Dip FMBM, CFL<sup>®</sup></div>
      <div class="person-contact">
        <div class="phone">0437 512 604</div>
        <div class="email">colin@brightledgeplan.com.au</div>
      </div>
    </div>
    <div class="brand"><span class="brand-mark"></span>BRIGHTLEDGE</div>
  </section>

</body>
</html>
```